Progressive/contemporary business card design for successful Startups as a Service Company

New logo launched in 2020. New website launched in 2021. Now that COVID is (mostly) behind us, I'm networking with more people and need a business card that matches the company/logo design aesthetic.

```html
<!DOCTYPE html>
<html lang="en">
<head>
<meta charset="utf-8">
<title>Quorvant Business Card</title>
<link href="https://fonts.googleapis.com/css2?family=Montserrat:wght@400;600&family=Raleway:wght@400&display=swap" rel="stylesheet">
<style>
  :root {
    --stage: #2a2a2a;
    --card-front: #ffffff;
    --card-back: #1e1e1e;
    --navy: #3e4a5f;
    --white: #ffffff;
    --muted: #c9c9c9;
    --faint: #262626;
    --divider: #d8d8d8;
    --icon-phone: #1aa3dd;
    --icon-mail: #4caf3f;
    --icon-home: #f26522;
  }
  html, body {
    margin: 0;
    padding: 0;
    width: 1200px;
    height: 583px;
    overflow: hidden;
    background: var(--stage);
  }
  .canvas {
    position: relative;
    width: 1200px;
    height: 583px;
  }
  .card {
    position: absolute;
    top: 137px;
    width: 515px;
    height: 309px;
    box-shadow: 0 10px 22px rgba(0,0,0,0.45);
  }
  .card--front {
    left: 68px;
    background: var(--card-front);
  }
  .card--back {
    left: 622px;
    background: var(--card-back);
  }
  .brand {
    position: absolute;
    left: 94px;
    top: 135px;
    display: flex;
    align-items: center;
    gap: 14px;
  }
  .brand__name {
    font-family: "Montserrat", sans-serif;
    font-weight: 400;
    font-size: 38px;
    letter-spacing: 9px;
    color: var(--navy);
    line-height: 1;
  }
  .brand__square {
    width: 34px;
    height: 34px;
    background: var(--navy);
  }
  .back__mark {
    position: absolute;
    left: 86px;
    top: 140px;
    width: 106px;
    text-align: center;
    font-family: "Montserrat", sans-serif;
    font-weight: 400;
    font-size: 13px;
    letter-spacing: 2px;
    color: var(--white);
  }
  .back__divider {
    position: absolute;
    left: 200px;
    top: 95px;
    width: 1px;
    height: 119px;
    background: var(--divider);
  }
  .contact {
    position: absolute;
    left: 212px;
    top: 108px;
  }
  .contact__name {
    margin: 0;
    font-family: "Montserrat", sans-serif;
    font-weight: 600;
    font-size: 18px;
    color: var(--white);
    line-height: 1;
  }
  .contact__role {
    margin: 4px 0 10px;
    font-family: "Raleway", sans-serif;
    font-size: 12.5px;
    color: var(--muted);
  }
  .contact__list {
    list-style: none;
    margin: 0;
    padding: 0;
  }
  .contact__item {
    display: flex;
    align-items: center;
    gap: 5px;
    height: 18px;
    font-family: "Raleway", sans-serif;
    font-size: 12.5px;
    color: var(--muted);
  }
  .contact__icon {
    width: 11px;
    height: 11px;
    flex: none;
  }
  .back__wordmark {
    position: absolute;
    right: 26px;
    bottom: 20px;
    font-family: "Montserrat", sans-serif;
    font-weight: 600;
    font-size: 28px;
    letter-spacing: 6px;
    color: var(--faint);
    line-height: 1;
  }
</style>
</head>
<body>
<div class="canvas">
  <section class="card card--front">
    <div class="brand">
      <span class="brand__name">QUORVANT</span>
      <span class="brand__square"></span>
    </div>
  </section>

  <section class="card card--back">
    <div class="back__mark">QUORVANT</div>
    <div class="back__divider"></div>
    <div class="contact">
      <h1 class="contact__name">MARA ELLING</h1>
      <p class="contact__role">Manager</p>
      <ul class="contact__list">
        <li class="contact__item">
          <svg class="contact__icon" viewBox="0 0 12 12" aria-hidden="true">
            <circle cx="6" cy="6" r="6" fill="var(--icon-phone)"/>
            <path d="M4 3.2 L5 3 L5.6 4.6 L5 5.2 Q5.6 6.5 6.8 7 L7.4 6.4 L9 7 L8.8 8 Q6.5 8.6 4.5 6.6 Q3.3 5 4 3.2Z" fill="#fff"/>
          </svg>
          555-014-229
        </li>
        <li class="contact__item">
          <svg class="contact__icon" viewBox="0 0 12 12" aria-hidden="true">
            <circle cx="6" cy="6" r="6" fill="var(--icon-mail)"/>
            <rect x="3" y="4" width="6" height="4.2" fill="#fff"/>
            <path d="M3 4 L6 6.3 L9 4" fill="none" stroke="var(--icon-mail)" stroke-width="0.8"/>
          </svg>
          hello@quorvant.co
        </li>
        <li class="contact__item">
          <svg class="contact__icon" viewBox="0 0 12 12" aria-hidden="true">
            <circle cx="6" cy="6" r="6" fill="var(--icon-home)"/>
            <path d="M6 2.8 L9 5.5 L8.2 5.5 L8.2 8.6 L3.8 8.6 L3.8 5.5 L3 5.5Z" fill="#fff"/>
            <rect x="5.3" y="6.6" width="1.4" height="2" fill="var(--icon-home)"/>
          </svg>
          Your address, your city, box 88900
        </li>
      </ul>
    </div>
    <div class="back__wordmark">QUORVANT</div>
  </section>
</div>
</body>
</html>
```